Roving Rotor Crew Van Wrap Project

In our busy world, you don’t have time to sit in a mechanic’s garage for hours to get your brakes replaced and you probably don’t want to deal with the inconvenience of dropping off a car, arranging rides, and being without a vehicle for a day or more. we’ve worked hard to create a convenient, affordable service designed to save you time and money.

Industry/Entity Type

Mechanic

Font styles to use
Sans Serif

Colors

Designer to choose colors to be used in the design.

Requirements
Must have
• 888-507-3962
• www.rovingrotorcrew-example.com
• We Come To You Home or Business
• Full Brake Service Repair
Should not have
• Don't want to wrap the whole vehicle. Want to just put letters and logo

```html
<!DOCTYPE html>
<html lang="en">
<head>
<meta charset="utf-8">
<title>Roving Rotor Crew – Van Lettering</title>
<link rel="stylesheet" href="https://fonts.googleapis.com/css2?family=Open+Sans:wght@600;700&display=swap">
<style>
  :root {
    --navy: #14192e;
    --red: #e0161b;
    --yellow: #f4b400;
    --white: #ffffff;
    --ink: #111111;
    --paper: #ffffff;
  }
  html, body {
    margin: 0;
    padding: 0;
    width: 1200px;
    height: 1200px;
    overflow: hidden;
    background: var(--paper);
  }
  .artboard {
    display: block;
    width: 1200px;
    height: 1200px;
    font-family: "Open Sans", sans-serif;
  }
  .band-navy { fill: var(--navy); }
  .band-red { fill: var(--red); }
  .band-yellow { fill: var(--yellow); }
  .edge-yellow { fill: none; stroke: var(--yellow); stroke-width: 5; }
  .edge-red { fill: none; stroke: var(--red); stroke-width: 4; }
  .brand-mark { fill: var(--navy); }
  .brand-name { fill: var(--navy); font-weight: 700; }
  .tagline-main { fill: var(--navy); font-weight: 700; font-size: 20px; }
  .tagline-sub { fill: var(--navy); font-weight: 600; font-size: 14px; }
  .phone-reverse { fill: var(--white); font-weight: 700; font-size: 36px; }
  .service-reverse { fill: var(--white); font-weight: 600; font-size: 35px; }
  .web-small { fill: var(--navy); font-weight: 700; font-size: 11px; }
  .phone-dark { fill: var(--ink); font-weight: 700; font-size: 29px; }
  .service-rear { fill: var(--white); font-weight: 600; font-size: 28px; }
  .arc-main { fill: var(--yellow); stroke: var(--navy); stroke-width: 0.6; font-weight: 700; font-size: 26px; }
  .arc-sub { fill: var(--red); font-weight: 700; font-size: 20px; }
</style>
</head>
<body>
<svg class="artboard" viewBox="0 0 1200 1200" xmlns="http://www.w3.org/2000/svg">
  <defs>
    <path id="arc-top" d="M490,640 Q600,585 710,640"/>
    <path id="arc-bottom" d="M510,660 Q600,615 690,660"/>
  </defs>

  <!-- Side panel lettering -->
  <g class="side-panel">
    <g class="brand-lockup">
      <circle class="brand-mark" cx="135" cy="152" r="13"/>
      <text class="brand-name" x="156" y="161" font-size="24">Roving Rotor Crew</text>
    </g>

    <g class="side-tagline">
      <text class="tagline-main" x="404" y="126" textLength="154" lengthAdjust="spacingAndGlyphs">We Come To You</text>
      <text class="tagline-sub" x="436" y="145" textLength="118" lengthAdjust="spacingAndGlyphs">Home or Business</text>
    </g>

    <g class="side-stripe">
      <polygon class="band-navy" points="250,232 345,232 440,340 870,340 860,400 352,400"/>
      <polyline class="edge-yellow" points="345,232 440,340 870,340"/>
      <polygon class="band-red" points="392,288 668,288 680,336 430,336"/>
      <line class="edge-red" x1="352" y1="402" x2="832" y2="402"/>
      <polygon class="band-yellow" points="620,404 832,404 826,428 630,428"/>
    </g>

    <text class="phone-reverse" x="420" y="326" textLength="232" lengthAdjust="spacingAndGlyphs">888-507-3962</text>
    <text class="service-reverse" x="386" y="388" textLength="424" lengthAdjust="spacingAndGlyphs">Full Brake Service Repair</text>
    <text class="web-small" x="638" y="421" textLength="180" lengthAdjust="spacingAndGlyphs">www.rovingrotorcrew-example.com</text>
  </g>

  <!-- Rear doors lettering -->
  <g class="rear-panel">
    <g class="rear-tagline">
      <text class="arc-main" text-anchor="middle"><textPath href="#arc-top" startOffset="50%">We Come To You</textPath></text>
      <text class="arc-sub" text-anchor="middle"><textPath href="#arc-bottom" startOffset="50%">Home or Business</textPath></text>
    </g>

    <g class="brand-lockup">
      <circle class="brand-mark" cx="600" cy="730" r="16"/>
      <text class="brand-name" x="600" y="800" font-size="34" text-anchor="middle">Roving Rotor Crew</text>
    </g>

    <text class="phone-dark" x="406" y="868" textLength="186" lengthAdjust="spacingAndGlyphs">888-507-3962</text>

    <g class="rear-service-block">
      <rect class="band-navy" x="602" y="856" width="206" height="100"/>
      <rect class="band-yellow" x="602" y="853" width="206" height="5"/>
      <rect class="band-red" x="602" y="953" width="206" height="5"/>
      <text class="service-rear" x="608" y="896" textLength="136" lengthAdjust="spacingAndGlyphs">Full Brake</text>
      <text class="service-rear" x="608" y="936" textLength="194" lengthAdjust="spacingAndGlyphs">Service Repair</text>
    </g>

    <text class="web-small" x="622" y="976" font-size="10.5" textLength="160" lengthAdjust="spacingAndGlyphs">www.rovingrotorcrew-example.com</text>
  </g>
</svg>
</body>
</html>
```